PowerPoint template design needed for sales and presales presentations

We would like to have a bright and light, contemporary PowerPoint design based on our existing style assets (see attached files).
We are based in Latvia. Our business is ERP systems implementation, IT infrastructure building and supporting our customers. We are moving from traditional Add-hoc projects model to standardized flat-rate offerings. Our technology platform is Quintavel.
The value proposition of our offerings is based around simplicity, transparency, quality, peace of mind, trust, easy of doing business.
I have to add that if any special are being used, they must be unicode to ensure proper Latvian language characters display.
Updates
Hi! The reason is an error at your side. Today it's 24/08/2020 when I started the project and made a payment. Still for some funny reason in the BRIEF I see that the project deadline is set to 20/08/2020. No wonder no designers are applying...
Target Market(s)
Small and medium enterprise
Look and feel

```html
<!DOCTYPE html>
<html lang="en">
<head>
<meta charset="utf-8">
<title>Lumora – Presentation Template</title>
<link href="https://fonts.googleapis.com/css2?family=Poppins:wght@300;400;500;600;700&display=swap" rel="stylesheet">
<style>
:root{
  --yellow:#ffc80a;
  --teal:#19b5ac;
  --green:#7dc242;
  --ink:#161616;
  --grey:#8a8a8a;
  --paper:#ffffff;
  --backdrop:#e6e7ea;
}
*{box-sizing:border-box;margin:0;padding:0}
html,body{width:1200px;height:2303px;overflow:hidden}
body{background:var(--backdrop);font-family:'Poppins',sans-serif;color:var(--ink);position:relative}
.abs{position:absolute}
.slide{position:absolute;width:384px;height:216px;background:var(--paper);overflow:hidden}
.c1{left:8px}.c2{left:408px}.c3{left:808px}
.r1{top:486px}.r2{top:713px}.r3{top:941px}.r4{top:1168px}
.r5{top:1396px}.r6{top:1623px}.r7{top:1851px}.r8{top:2078px}

/* brand */
.brand{position:absolute;display:flex;align-items:center;gap:4px;white-space:nowrap}
.brand-dot{display:block;border-radius:50%;background:currentColor;flex:none}
.brand-name{font-weight:600;letter-spacing:.1em;line-height:1}

/* header bar */
.hdr{position:absolute;left:0;top:0;width:100%;height:28px;background:var(--ink)}
.hdr-title{position:absolute;left:6px;top:4px;color:#fff;font-weight:700;font-size:14px}
.hdr .brand{right:8px;top:10px;color:#fff;gap:3px}
.hdr .brand-dot{width:6px;height:6px}
.hdr .brand-name{font-size:7px}
.stripe{position:absolute;left:0;top:28px;width:100%;height:5px}

/* footer */
.ftr{position:absolute;left:0;bottom:0;width:100%;height:14px}
.ftr-copy{position:absolute;right:10px;bottom:3px;font-size:3.6px;color:var(--ink);font-weight:500}
.ftr-dark .ftr-copy{color:#fff}
.pgnum{position:absolute;left:26px;bottom:4px;font-size:3.6px}

.p{font-size:4.2px;line-height:1.55;color:#333}
.p-grey{color:#777}
.h-sub{font-size:4.5px;letter-spacing:.35em;font-weight:600;color:var(--teal)}
.pill{position:absolute;border-radius:8px;color:#fff;font-weight:700;font-size:4.5px;display:flex;align-items:center;padding-left:5px}
.dot{position:absolute;border-radius:50%}
.ph{position:absolute}
</style>
</head>
<body>

<!-- Hero title slide -->
<section class="slide" style="left:320px;top:70px;width:560px;height:315px;background:#2a2522" aria-label="Title slide">
  <div class="ph" role="img" aria-label="Dark background photo with faint hexagon network" style="left:0;top:0;width:560px;height:260px;background:linear-gradient(120deg,#221e1c 0%,#3a3330 55%,#2c2d30 100%)"></div>
  <div class="brand" style="left:52px;top:58px;color:#fff;gap:6px"><span class="brand-dot" style="width:12px;height:12px"></span><span class="brand-name" style="font-size:16px">LUMORA</span></div>
  <div class="abs" style="left:52px;top:126px;color:#fff;font-size:22px;font-weight:600">PRESTATION TITLE GOES HERE</div>
  <div class="abs" style="left:52px;top:158px;color:#fff;font-size:6px;letter-spacing:.4em;font-weight:700">SUB TITLE GOES HERE</div>
  <div class="abs" style="left:52px;top:204px;color:#fff;font-size:6px;letter-spacing:.4em;font-weight:700">2020</div>
  <svg class="abs" style="left:0;top:252px" width="560" height="8"><rect width="200" height="8" fill="#fff"/><rect x="200" y="2" width="120" height="4" fill="var(--yellow)"/><rect x="320" y="2" width="130" height="4" fill="var(--green)"/><rect x="450" y="2" width="110" height="4" fill="var(--teal)"/></svg>
  <div class="abs" style="left:0;top:260px;width:560px;height:55px;background:#fff"></div>
</section>

<!-- Row 1 -->
<section class="slide c1 r1" style="background:var(--yellow)">
  <div class="brand" style="left:27px;top:56px;color:var(--ink)"><span class="brand-dot" style="width:8px;height:8px"></span><span class="brand-name" style="font-size:11px">LUMORA</span></div>
  <div class="abs" style="left:27px;top:100px;font-size:15px;font-weight:600">PRESTATION TITLE GOES HERE</div>
  <div class="abs" style="left:27px;top:122px;font-size:4.5px;letter-spacing:.4em;font-weight:700">SUB TITLE GOES HERE</div>
  <div class="pill" style="left:27px;top:163px;width:93px;height:16px;background:var(--ink);font-size:4.2px">PRESENTER NAME</div>
</section>
<section class="slide c2 r1" style="background:var(--teal)">
  <div class="brand" style="left:27px;top:60px;color:#fff"><span class="brand-dot" style="width:8px;height:8px"></span><span class="brand-name" style="font-size:11px">LUMORA</span></div>
  <div class="abs" style="left:27px;top:100px;font-size:15px;font-weight:600;color:#fff">PRESTATION TITLE GOES HERE</div>
  <div class="abs" style="left:27px;top:122px;font-size:4.5px;letter-spacing:.4em;font-weight:700;color:#fff">SUB TITLE GOES HERE</div>
  <div class="pill" style="left:27px;top:163px;width:93px;height:16px;background:#fff;color:var(--teal);font-size:4.2px">PRESENTER NAME</div>
</section>
<section class="slide c3 r1">
  <div class="brand" style="left:170px;top:14px;color:var(--ink)"><span class="brand-dot" style="width:6px;height:6px"></span><span class="brand-name" style="font-size:8px">LUMORA</span></div>
  <div class="ph" role="img" aria-label="Photo of hands working on a laptop" style="left:0;top:36px;width:384px;height:166px;background:linear-gradient(100deg,#1d1c1c,#3a3432 60%,#6b5d52)"></div>
  <div class="abs" style="left:78px;top:100px;font-size:15px;font-weight:600;color:#fff">PRESTATION TITLE GOES HERE</div>
  <div class="abs" style="left:150px;top:124px;font-size:4.5px;letter-spacing:.4em;font-weight:700;color:#fff">SUB TITLE GOES HERE</div>
  <div class="pill" style="left:152px;top:156px;width:91px;height:16px;background:var(--green);font-size:4.2px;padding-left:20px">PRESENTER NAME</div>
</section>

<!-- Row 2 -->
<section class="slide c1 r2">
  <div class="hdr"><div class="hdr-title">Title Text Here</div><div class="brand"><span class="brand-dot"></span><span class="brand-name">LUMORA</span></div></div>
  <svg class="stripe" viewBox="0 0 384 5" preserveAspectRatio="none"><rect width="150" height="5" fill="var(--ink)"/><rect x="150" width="30" height="3" fill="var(--teal)"/><rect x="180" width="30" height="3" fill="var(--green)"/><rect x="210" width="30" height="3" fill="var(--yellow)"/></svg>
  <div class="abs p" style="left:22px;top:62px;width:340px">Lorem ipsum dolor sit amet, consectetur adipiscing elit, sed do eiusmod tempor incididunt ut labore et dolore magna aliqua. Ut enim ad minim veniam, quis nostrud exercitation ullamco laboris nisi ut aliquip ex ea commodo.<br><br>Lorem ipsum dolor sit amet, consectetur adipiscing elit, sed do eiusmod tempor incididunt ut labore et dolore magna aliqua. Lorem ipsum dolor sit amet, consectetur adipiscing elit, sed do eiusmod tempor incididunt ut labore. Ut enim ad minim veniam, quis nostrud exercitation ullamco laboris.<br><br>Lorem ipsum dolor sit amet, consectetur adipiscing elit, sed do eiusmod tempor incididunt ut labore et dolore magna aliqua. Sed do eiusmod tempor incididunt ut labore et dolore magna aliqua. Lorem ipsum dolor sit amet, consectetur adipiscing elit, sed do eiusmod tempor incididunt ut labore et dolore magna aliqua. Ut enim ad minim veniam.<br><br>Lorem ipsum dolor sit amet, consectetur adipiscing elit, sed do eiusmod tempor incididunt ut labore et dolore magna aliqua.</div>
  <div class="pgnum">5</div><div class="ftr-copy">Copyright © | All Rights Reserved</div>
</section>
<section class="slide c2 r2">
  <div class="abs" style="left:27px;top:92px;font-size:12px;font-weight:600">Heading + Text Slide</div>
  <div class="abs h-sub" style="left:27px;top:110px">SUB TITLE GOES HERE</div>
  <div class="dot" style="left:215px;top:36px;width:20px;height:20px;background:var(--teal)"></div>
  <div class="dot" style="left:215px;top:71px;width:20px;height:20px;background:var(--yellow)"></div>
  <div class="dot" style="left:215px;top:105px;width:20px;height:20px;background:var(--green)"></div>
  <div class="dot" style="left:215px;top:140px;width:20px;height:20px;background:var(--ink)"></div>
  <div class="abs" style="left:245px;top:36px;font-size:4.5px;color:var(--teal);font-weight:500">Your Text Here</div>
  <div class="abs p p-grey" style="left:245px;top:43px;width:90px">Lorem ipsum dolor sit amet, nec an dictas equidem appellantur, ut has commune.</div>
  <div class="abs" style="left:245px;top:71px;font-size:4.5px;color:var(--yellow);font-weight:500">Your Text Here</div>
  <div class="abs p p-grey" style="left:245px;top:78px;width:90px">Lorem ipsum dolor sit amet, nec an dictas equidem appellantur, ut has commune.</div>
  <div class="abs" style="left:245px;top:105px;font-size:4.5px;color:var(--green);font-weight:500">Your Text Here</div>
  <div class="abs p p-grey" style="left:245px;top:112px;width:90px">Lorem ipsum dolor sit amet, nec an dictas equidem appellantur, ut has commune.</div>
  <div class="abs" style="left:245px;top:140px;font-size:4.5px;font-weight:500">Your Text Here</div>
  <div class="abs p p-grey" style="left:245px;top:147px;width:90px">Lorem ipsum dolor sit amet, nec an dictas equidem appellantur, ut has commune.</div>
  <svg class="ftr" viewBox="0 0 384 14" preserveAspectRatio="none"><rect y="2" width="384" height="12" fill="var(--ink)"/><polygon points="150,0 210,0 214,3 154,3" fill="var(--yellow)"/><polygon points="210,0 270,0 274,3 214,3" fill="var(--green)"/><polygon points="270,0 384,0 384,3 274,3" fill="var(--teal)"/></svg>
  <div class="ftr-dark"><div class="ftr-copy">Copyright © | All Rights Reserved</div></div>
</section>
<section class="slide c3 r2">
  <div class="abs" style="left:24px;top:40px;font-size:15px;font-weight:600;line-height:1.4">Here add some<br>short text to <span style="color:var(--yellow)">explain</span><br><span style="color:var(--green)">some things</span></div>
  <div class="abs" style="left:196px;top:110px;font-size:24px;font-weight:600;color:var(--yellow)">56%</div>
  <div class="abs p p-grey" style="left:252px;top:94px;width:110px;text-align:justify">Lorem ipsum dolor sit amet. Etiam et kur palta consectetur adipiscing elit. Fusce sit amet neque iaculis factur aticur at dat.</div>
  <div class="abs p p-grey" style="left:195px;top:140px;width:167px;text-align:justify">sodales ex eu, efficitur lacus. Cras imperdiet, nulla nec sagittis pulvinar, neque augue iaculis risus, ac fringilla felis urna fermentum mi. Ut vehicula vel enim sit amet vulputate.</div>
  <svg class="ftr" viewBox="0 0 384 14" preserveAspectRatio="none"><rect y="2" width="384" height="12" fill="var(--ink)"/><polygon points="150,0 210,0 214,3 154,3" fill="var(--yellow)"/><polygon points="210,0 270,0 274,3 214,3" fill="var(--green)"/><polygon points="270,0 384,0 384,3 274,3" fill="var(--teal)"/></svg>
  <div class="ftr-dark"><div class="ftr-copy">Copyright © | All Rights Reserved</div></div>
</section>

<!-- Row 3 -->
<section class="slide c1 r3">
  <div class="ph" role="img" aria-label="Photo of a team gathered around a laptop" style="left:0;top:0;width:255px;height:155px;background:linear-gradient(120deg,#d9d3cc,#8c7a6c 55%,#4b3f38)"></div>
  <div class="abs" style="left:193px;top:30px;width:102px;height:92px;background:var(--green);border-radius:6px;padding:14px 10px;color:#fff">
    <div style="font-size:18px;font-weight:700;opacity:.4;line-height:.8">01</div>
    <div style="font-size:5.5px;font-weight:500;margin-top:-6px">Your Text Here</div>
    <div style="font-size:4.4px;line-height:1.5;margin-top:6px">Lorem ipsum dolor sit amet, consectetur adipiscing elit, sed do eiusmod tempor incidunt ut labore et dolore magna aliqua.</div>
  </div>
  <div class="abs" style="left:25px;top:163px;font-size:19px;font-weight:600">Heading + Text + Image Slide</div>
  <svg class="ftr" viewBox="0 0 384 14" preserveAspectRatio="none"><rect y="2" width="384" height="12" fill="var(--ink)"/><polygon points="150,0 210,0 214,3 154,3" fill="var(--yellow)"/><polygon points="210,0 270,0 274,3 214,3" fill="var(--green)"/><polygon points="270,0 384,0 384,3 274,3" fill="var(--teal)"/></svg>
  <div class="ftr-dark"><div class="ftr-copy">Copyright © | All Rights Reserved</div></div>
</section>
<section class="slide c2 r3">
  <div class="hdr"><div class="hdr-title">Add Awesome Title Here</div><div class="brand"><span class="brand-dot"></span><span class="brand-name">LUMORA</span></div></div>
  <svg class="stripe" viewBox="0 0 384 5" preserveAspectRatio="none"><rect width="210" height="5" fill="var(--ink)"/><rect x="210" width="30" height="3" fill="var(--teal)"/><rect x="240" width="30" height="3" fill="var(--green)"/><rect x="270" width="30" height="3" fill="var(--yellow)"/></svg>
  <div class="abs p" style="left:24px;top:48px;width:150px;text-align:justify">Lorem ipsum dolor sit amet, consectetur adipiscing elit, sed do eiusmod tempor incididunt ut labore et dolore magna aliqua. Lorem ipsum dolor sit amet, consectetur adipiscing elit, sed do eiusmod tempor incididunt ut labore et dolore magna aliqua.<br><br>sed do eiusmod tempor incididunt ut labore et dolore magna aliqua. Lorem ipsum dolor sit amet, consectetur adipiscing elit, sed do eiusmod tempor incididunt ut labore et dolore magna aliqua. Lorem ipsum dolor sit amet, consectetur adipiscing elit, sed do eiusmod tempor incididunt ut labore et dolore magna aliqua. Lorem ipsum dolor sit amet, consectetur adipiscing elit, sed do eiusmod tempor incididunt ut labore et dolore magna aliqua. Ut enim ad minim veniam, quis nostrud exercitation ullamco laboris nisi ut aliquip.</div>
  <div class="abs" style="left:192px;top:60px;width:168px;height:54px;background:var(--yellow);border-radius:5px;color:#fff;font-size:4.4px;text-align:center;padding:14px 14px;line-height:1.6">Lorem ipsum the printing and typesetting industry. Lorem Ipsum has been the industry's standard dummy text ever since the 1500s, when an unknown printer took</div>
  <div class="abs" style="left:192px;top:123px;width:168px;height:54px;background:var(--green);border-radius:5px;color:#fff;font-size:4.4px;text-align:center;padding:14px 14px;line-height:1.6">Lorem ipsum the printing and typesetting industry. Lorem Ipsum has been the industry's standard dummy text ever since the 1500s, when an unknown printer took</div>
  <div class="pgnum">9</div><div class="ftr-copy">Copyright © | All Rights Reserved</div>
</section>
<section class="slide c3 r3">
  <div class="hdr"><div class="hdr-title">Text + Image Slide</div><div class="brand"><span class="brand-dot"></span><span class="brand-name">LUMORA</span></div></div>
  <svg class="stripe" viewBox="0 0 384 5" preserveAspectRatio="none"><rect width="180" height="5" fill="var(--ink)"/><rect x="180" width="30" height="3" fill="var(--teal)"/><rect x="210" width="30" height="3" fill="var(--green)"/><rect x="240" width="30" height="3" fill="var(--yellow)"/></svg>
  <div class="abs p" style="left:30px;top:60px;width:135px">sed do eiusmod tempor incididunt ut labore et dolore magna aliqua. Lorem ipsum dolor sit amet, consectetur adipiscing elit, sed do eiusmod tempor incididunt ut labore et dolore magna aliqua. Lorem ipsum dolor sit amet, consectetur adipiscing elit, sed do eiusmod tempor.</div>
  <div class="dot" style="left:30px;top:103px;width:20px;height:20px;background:var(--green)"></div>
  <div class="abs" style="left:60px;top:103px;font-size:4.8px;color:var(--green)">Project name</div>
  <div class="abs p p-grey" style="left:60px;top:110px;width:105px">Lorem ipsum dolor sit amet, nec an dictas equidem appellantur, ut has commune.</div>
  <div class="dot" style="left:30px;top:143px;width:20px;height:20px;background:var(--teal)"></div>
  <div class="abs" style="left:60px;top:143px;font-size:4.8px;color:var(--teal)">Project name</div>
  <div class="abs p p-grey" style="left:60px;top:150px;width:105px">Lorem ipsum dolor sit amet, nec an dictas equidem appellantur, ut has commune.</div>
  <div class="ph" role="img" aria-label="Photo of a glowing digital globe above an open hand" style="left:199px;top:44px;width:165px;height:148px;border-radius:10px;background:radial-gradient(circle at 50% 40%,#8fc4ee,#2d5f9c 45%,#0d1f46)"></div>
  <div class="pgnum">10</div><div class="ftr-copy">Copyright © | All Rights Reserved</div>
</section>

<!-- Row 4 -->
<section class="slide c1 r4">
  <div class="ph" role="img" aria-label="Teal-tinted photo of a glass office tower" style="left:0;top:0;width:172px;height:216px;background:linear-gradient(160deg,#6ed3cc,#19b5ac 60%,#128a84)"></div>
  <div class="abs" style="left:38px;top:71px;width:120px;color:#fff;font-size:9px;line-height:1.3">SUCCESS IS NOT ONLY WHAT YOU ACHIEVE IN YOUR LIFE, BUT ALSO WHAT YOU INSPIRE IN THE LIVES OF OTHERS</div>
  <div class="brand" style="left:330px;top:12px;color:var(--ink);gap:3px"><span class="brand-dot" style="width:5px;height:5px"></span><span class="brand-name" style="font-size:6px">LUMORA</span></div>
  <div class="abs p" style="left:196px;top:42px;width:165px;color:var(--green)">Lorem ipsum dolor sit amet, consectetur adipiscing elit. Fusce sit amet neque sodales, faucibus arcu efficitur lacus. Cras imperdiet, nulla nec sagittis pulvinar, neque augue iaculis risus, ac fringilla felis urna fermentum mi.</div>
  <div class="dot" style="left:196px;top:83px;width:11px;height:11px;background:var(--green)"></div>
  <div class="abs p" style="left:213px;top:78px;width:150px"><b>Contents Title</b><br>Lorem ipsum randomised words which don't look even slightly believable in some form, by injected humour.</div>
  <div class="dot" style="left:196px;top:122px;width:11px;height:11px;background:var(--green)"></div>
  <div class="abs p" style="left:213px;top:117px;width:150px"><b>Contents Title</b><br>Lorem ipsum randomised words which don't look even slightly believable in some form, by injected humour.</div>
  <div class="dot" style="left:196px;top:160px;width:11px;height:11px;background:var(--green)"></div>
  <div class="abs p" style="left:213px;top:155px;width:150px"><b>Contents Title</b><br>Lorem ipsum randomised words which don't look even slightly believable in some form, by injected humour.</div>
  <div class="ftr-copy">Copyright © | All Rights Reserved</div>
</section>
<section class="slide c2 r4">
  <div class="hdr"><div class="hdr-title">Your Title Here</div><div class="brand"><span class="brand-dot"></span><span class="brand-name">LUMORA</span></div></div>
  <svg class="stripe" viewBox="0 0 384 5" preserveAspectRatio="none"><rect width="210" height="5" fill="var(--ink)"/><rect x="210" width="30" height="3" fill="var(--teal)"/><rect x="240" width="30" height="3" fill="var(--green)"/><rect x="270" width="30" height="3" fill="var(--yellow)"/></svg>
  <svg class="abs" style="left:30px;top:68px" width="100" height="90" viewBox="0 0 100 90">
    <circle cx="45" cy="45" r="40" fill="#fff" stroke="var(--ink)" stroke-width="6"/>
    <circle cx="45" cy="45" r="32" fill="var(--teal)"/>
    <circle cx="45" cy="45" r="24" fill="#fff" stroke="var(--ink)" stroke-width="3"/>
    <circle cx="45" cy="45" r="17" fill="var(--green)"/>
    <circle cx="45" cy="45" r="6" fill="#fff" stroke="var(--ink)" stroke-width="2"/>
    <line x1="45" y1="45" x2="95" y2="45" stroke="var(--ink)" stroke-width="3"/>
    <polygon points="82,38 96,45 82,52 86,45" fill="var(--yellow)"/>
  </svg>
  <div class="pill" style="left:152px;top:45px;width:88px;height:10px;background:var(--green)">Lorem ipsum dolor</div>
  <div class="abs p p-grey" style="left:154px;top:60px;width:92px">Lorem ipsum dolor sit amet, consectetur adipiscing elit, sed do eiusmod tempor</div>
  <div class="pill" style="left:268px;top:45px;width:88px;height:10px;background:var(--green)">Lorem ipsum dolor</div>
  <div class="abs p p-grey" style="left:270px;top:60px;width:92px">Lorem ipsum dolor sit amet, consectetur adipiscing elit, sed do eiusmod tempor</div>
  <div class="pill" style="left:152px;top:94px;width:88px;height:10px;background:var(--green)">Lorem ipsum dolor</div>
  <div class="abs p p-grey" style="left:154px;top:109px;width:92px">Lorem ipsum dolor sit amet, consectetur adipiscing elit, sed do eiusmod tempor</div>
  <div class="pill" style="left:268px;top:94px;width:88px;height:10px;background:var(--green)">Lorem ipsum dolor</div>
  <div class="abs p p-grey" style="left:270px;top:109px;width:92px">Lorem ipsum dolor sit amet, consectetur adipiscing elit, sed do eiusmod tempor</div>
  <div class="pill" style="left:152px;top:143px;width:88px;height:10px;background:var(--green)">Lorem ipsum dolor</div>
  <div class="abs p p-grey" style="left:154px;top:158px;width:92px">Lorem ipsum dolor sit amet, consectetur adipiscing elit, sed do eiusmod tempor</div>
  <div class="pill" style="left:268px;top:143px;width:88px;height:10px;background:var(--green)">Lorem ipsum dolor</div>
  <div class="abs p p-grey" style="left:270px;top:158px;width:92px">Lorem ipsum dolor sit amet, consectetur adipiscing elit, sed do eiusmod tempor</div>
  <div class="pgnum">11</div><div class="ftr-copy">Copyright © | All Rights Reserved</div>
</section>
<section class="slide c3 r4">
  <div class="abs" style="left:27px;top:94px;font-size:12px;font-weight:600">Heading + Map</div>
  <div class="abs h-sub" style="left:27px;top:111px">SUB TITLE GOES HERE</div>
  <div class="ph" role="img" aria-label="Map of Europe with several countries highlighted in green" style="left:190px;top:10px;width:190px;height:185px;border-radius:40% 20% 30% 40%;background:radial-gradient(circle at 60% 45%,#bfe3a0,#e4e6e8 70%)"></div>
  <svg class="ftr" viewBox="0 0 384 14" preserveAspectRatio="none"><rect y="2" width="384" height="12" fill="var(--ink)"/><polygon points="150,0 210,0 214,3 154,3" fill="var(--yellow)"/><polygon points="210,0 270,0 274,3 214,3" fill="var(--green)"/><polygon points="270,0 384,0 384,3 274,3" fill="var(--teal)"/></svg>
  <div class="ftr-dark"><div class="ftr-copy">Copyright © | All Rights Reserved</div></div>
</section>

<!-- Row 5 -->
<section class="slide c1 r5">
  <div class="hdr"><div class="hdr-title">Infographic</div><div class="brand"><span class="brand-dot"></span><span class="brand-name">LUMORA</span></div></div>
  <svg class="stripe" viewBox="0 0 384 5" preserveAspectRatio="none"><rect width="150" height="5" fill="var(--ink)"/><rect x="150" width="30" height="3" fill="var(--teal)"/><rect x="180" width="30" height="3" fill="var(--green)"/><rect x="210" width="30" height="3" fill="var(--yellow)"/></svg>
  <svg class="abs" style="left:130px;top:55px" width="124" height="124" viewBox="0 0 124 124">
    <g fill="none" stroke-width="22" transform="rotate(-90 62 62)">
      <circle cx="62" cy="62" r="48" stroke="var(--green)" stroke-dasharray="46 256"/>
      <circle cx="62" cy="62" r="48" stroke="var(--teal)" stroke-dasharray="46 256" stroke-dashoffset="-50"/>
      <circle cx="62" cy="62" r="48" stroke="var(--teal)" stroke-dasharray="46 256" stroke-dashoffset="-100"/>
      <circle cx="62" cy="62" r="48" stroke="var(--yellow)" stroke-dasharray="46 256" stroke-dashoffset="-150"/>
      <circle cx="62" cy="62" r="48" stroke="var(--green)" stroke-dasharray="46 256" stroke-dashoffset="-200"/>
      <circle cx="62" cy="62" r="48" stroke="var(--yellow)" stroke-dasharray="46 256" stroke-dashoffset="-250"/>
    </g>
    <circle cx="62" cy="62" r="4" fill="var(--ink)"/>
  </svg>
  <div class="abs" style="left:56px;top:58px;font-size:4.8px;font-weight:600;text-align:center;width:90px">LOREM IPSUM DOLOR</div>
  <div class="abs p p-grey" style="left:50px;top:65px;width:100px;text-align:center">Lorem ipsum dolor sit amet, consectetur adipiscing elit, sed do eiusmod tempor</div>
  <div class="abs" style="left:31px;top:110px;font-size:4.8px;font-weight:600;text-align:center;width:90px">LOREM IPSUM DOLOR</div>
  <div class="abs p p-grey" style="left:25px;top:117px;width:100px;text-align:center">Lorem ipsum dolor sit amet, consectetur adipiscing elit, sed do eiusmod tempor</div>
  <div class="abs" style="left:56px;top:162px;font-size:4.8px;font-weight:600;text-align:center;width:90px">LOREM IPSUM DOLOR</div>
  <div class="abs p p-grey" style="left:50px;top:169px;width:100px;text-align:center">Lorem ipsum dolor sit amet, consectetur adipiscing elit, sed do eiusmod tempor</div>
  <div class="abs" style="left:248px;top:58px;font-size:4.8px;font-weight:600">LOREM IPSUM DOLOR</div>
  <div class="abs p p-grey" style="left:248px;top:65px;width:100px">Lorem ipsum dolor sit amet, consectetur adipiscing elit, sed do eiusmod tempor</div>
  <div class="abs" style="left:270px;top:110px;font-size:4.8px;font-weight:600">LOREM IPSUM DOLOR</div>
  <div class="abs p p-grey" style="left:270px;top:117px;width:100px">Lorem ipsum dolor sit amet, consectetur adipiscing elit, sed do eiusmod tempor</div>
  <div class="abs" style="left:250px;top:162px;font-size:4.8px;font-weight:600">LOREM IPSUM DOLOR</div>
  <div class="abs p p-grey" style="left:250px;top:169px;width:100px">Lorem ipsum dolor sit amet, consectetur adipiscing elit, sed do eiusmod tempor</div>
  <div class="ftr-copy">Copyright © | All Rights Reserved</div>
</section>
<section class="slide c2 r5">
  <div class="hdr"><div class="hdr-title">Your Title Here</div><div class="brand"><span class="brand-dot"></span><span class="brand-name">LUMORA</span></div></div>
  <svg class="stripe" viewBox="0 0 384 5" preserveAspectRatio="none"><rect width="210" height="5" fill="var(--ink)"/><rect x="210" width="30" height="3" fill="var(--teal)"/><rect x="240" width="30" height="3" fill="var(--green)"/><rect x="270" width="30" height="3" fill="var(--yellow)"/></svg>
  <div class="abs p" style="left:22px;top:56px;width:165px;text-align:justify">Lorem ipsum dolor sit amet, consectetur adipiscing elit, sed do eiusmod tempor incididunt ut labore et dolore magna aliqua. Lorem ipsum dolor sit amet, consectetur adipiscing elit, sed do eiusmod tempor incididunt ut labore et dolore magna aliqua. Ut enim ad minim veniam, quis nostrud exercitation ullamco laboris nisi ut aliquip.<br><br>Lorem ipsum dolor sit amet, consectetur adipiscing elit, sed do eiusmod tempor incididunt ut labore et dolore magna aliqua. Lorem ipsum dolor sit amet, consectetur adipiscing elit, sed do eiusmod tempor incididunt ut labore et dolore magna aliqua. Ut enim ad minim veniam, quis nostrud exercitation.<br><br>Lorem ipsum dolor sit amet, consectetur adipiscing elit, sed do eiusmod tempor incididunt ut labore et dolore magna aliqua. Lorem ipsum dolor sit amet, consectetur adipiscing elit, sed do eiusmod tempor incididunt ut labore. Ut enim ad minim veniam, quis nostrud exercitation ullamco laboris nisi ut aliquip.</div>
  <svg class="abs" style="left:205px;top:66px" width="170" height="115" viewBox="0 0 170 115" font-family="Poppins, sans-serif" font-size="4.5" fill="#fff" text-anchor="middle">
    <polygon points="70,0 100,0 108,20 62,20" fill="var(--teal)"/><text x="85" y="9">Lorem ipsum</text><text x="85" y="15">dolor</text>
    <polygon points="60,26 110,26 118,46 52,46" fill="var(--yellow)"/><text x="85" y="38">Lorem ipsum dolor</text>
    <polygon points="50,52 120,52 128,72 42,72" fill="var(--green)"/><text x="85" y="64">Lorem ipsum dolor</text>
    <polygon points="40,78 130,78 140,100 30,100" fill="var(--teal)"/><text x="85" y="91">Lorem ipsum dolor</text>
  </svg>
  <div class="pgnum">14</div><div class="ftr-copy">Copyright © | All Rights Reserved</div>
</section>
<section class="slide c3 r5">
  <div class="abs" style="left:0;top:26px;width:384px;text-align:center;font-size:17px;font-weight:600">Your <span style="color:var(--yellow)">awesome</span> text here</div>
  <div class="abs p p-grey" style="left:48px;top:53px;width:290px;text-align:center">Lorem ipsum the printing and typesetting industry. Lorem ipsum has been the industry's standard dummy text ever since the 1500s, when an unknown printer took a galley of type and scrambled it to make a type specimen book. It has survived not only five centuries.</div>
  <svg class="abs" style="left:75px;top:90px" width="240" height="60" viewBox="0 0 240 60" font-family="Poppins, sans-serif" font-size="11" font-weight="600" text-anchor="middle">
    <g fill="none" stroke-width="3">
      <circle cx="30" cy="30" r="26" stroke="#e2e2e2"/><circle cx="30" cy="30" r="26" stroke="var(--green)" stroke-dasharray="81.7 163.4" transform="rotate(-90 30 30)"/>
      <circle cx="120" cy="30" r="26" stroke="#e2e2e2"/><circle cx="120" cy="30" r="26" stroke="var(--teal)" stroke-dasharray="122.5 163.4" transform="rotate(-90 120 30)"/>
      <circle cx="210" cy="30" r="26" stroke="#e2e2e2"/><circle cx="210" cy="30" r="26" stroke="var(--yellow)" stroke-dasharray="65.3 163.4" transform="rotate(-90 210 30)"/>
    </g>
    <text x="30" y="34" fill="var(--green)">50%</text><text x="120" y="34" fill="var(--teal)">75%</text><text x="210" y="34" fill="var(--yellow)">40%</text>
  </svg>
  <div class="abs p p-grey" style="left:80px;top:158px;width:50px;text-align:center">Lorem ipsum dolor amet consectetur dolor</div>
  <div class="abs p p-grey" style="left:170px;top:158px;width:50px;text-align:center">Lorem ipsum dolor amet consectetur dolor</div>
  <div class="abs p p-grey" style="left:260px;top:158px;width:50px;text-align:center">Lorem ipsum dolor amet consectetur dolor</div>
  <svg class="ftr" viewBox="0 0 384 14" preserveAspectRatio="none"><rect y="2" width="384" height="12" fill="var(--ink)"/><polygon points="150,0 210,0 214,3 154,3" fill="var(--yellow)"/><polygon points="210,0 270,0 274,3 214,3" fill="var(--green)"/><polygon points="270,0 384,0 384,3 274,3" fill="var(--teal)"/></svg>
  <div class="ftr-dark"><div class="ftr-copy">Copyright © | All Rights Reserved</div></div>
</section>

<!-- Row 6 -->
<section class="slide c1 r6">
  <div class="hdr"><div class="hdr-title">Add Awesome Title Here</div><div class="brand"><span class="brand-dot"></span><span class="brand-name">LUMORA</span></div></div>
  <svg class="stripe" viewBox="0 0 384 5" preserveAspectRatio="none"><rect width="210" height="5" fill="var(--ink)"/><rect x="210" width="30" height="3" fill="var(--teal)"/><rect x="240" width="30" height="3" fill="var(--green)"/><rect x="270" width="30" height="3" fill="var(--yellow)"/></svg>
  <svg class="abs" style="left:25px;top:65px" width="340" height="110" viewBox="0 0 340 110" font-family="Poppins, sans-serif">
    <g fill="var(--teal)">
      <circle cx="6" cy="8" r="6"/><circle cx="6" cy="36" r="6"/><circle cx="6" cy="65" r="6"/><circle cx="6" cy="93" r="6"/>
      <circle cx="118" cy="8" r="6"/><circle cx="118" cy="36" r="6"/><circle cx="118" cy="65" r="6"/><circle cx="118" cy="93" r="6"/>
      <circle cx="232" cy="8" r="6"/><circle cx="232" cy="36" r="6"/><circle cx="232" cy="65" r="6"/><circle cx="232" cy="93" r="6"/>
    </g>
    <g fill="#fff" font-size="4" font-weight="700" text-anchor="middle">
      <text x="6" y="9.5">01</text><text x="6" y="37.5">04</text><text x="6" y="66.5">07</text><text x="6" y="94.5">10</text>
      <text x="118" y="9.5">02</text><text x="118" y="37.5">05</text><text x="118" y="66.5">08</text><text x="118" y="94.5">11</text>
      <text x="232" y="9.5">03</text><text x="232" y="37.5">06</text><text x="232" y="66.5">09</text><text x="232" y="94.5">12</text>
    </g>
    <g font-size="4.6" font-weight="500" fill="var(--ink)">
      <text x="17" y="7">Your Text Here</text><text x="17" y="35">Your Text Here</text><text x="17" y="64">Your Text Here</text><text x="17" y="92">Your Text Here</text>
      <text x="129" y="7">Your Text Here</text><text x="129" y="35">Your Text Here</text><text x="129" y="64">Your Text Here</text><text x="129" y="92">Your Text Here</text>
      <text x="243" y="7">Your Text Here</text><text x="243" y="35">Your Text Here</text><text x="243" y="64">Your Text Here</text><text x="243" y="92">Your Text Here</text>
    </g>
    <g font-size="4" fill="#999">
      <text x="17" y="13">Lorem ipsum dolor sit amet</text><text x="17" y="41">Lorem ipsum dolor sit amet</text><text x="17" y="70">Lorem ipsum dolor sit amet</text><text x="17" y="98">Lorem ipsum dolor sit amet</text>
      <text x="129" y="13">Lorem ipsum dolor sit amet</text><text x="129" y="41">Lorem ipsum dolor sit amet</text><text x="129" y="70">Lorem ipsum dolor sit amet</text><text x="129" y="98">Lorem ipsum dolor sit amet</text>
      <text x="243" y="13">Lorem ipsum dolor sit amet</text><text x="243" y="41">Lorem ipsum dolor sit amet</text><text x="243" y="70">Lorem ipsum dolor sit amet</text><text x="243" y="98">Lorem ipsum dolor sit amet</text>
    </g>
  </svg>
  <div class="abs" style="left:16px;top:197px;width:352px;height:1px;background:#ddd"></div>
  <div class="ftr-copy">Copyright © | All Rights Reserved</div>
</section>
<section class="slide c2 r6">
  <div class="hdr"><div class="brand"><span class="brand-dot"></span><span class="brand-name">LUMORA</span></div></div>
  <svg class="stripe" viewBox="0 0 384 5" preserveAspectRatio="none"><rect width="150" height="5" fill="var(--ink)"/><rect x="150" width="30" height="3" fill="var(--teal)"/><rect x="180" width="30" height="3" fill="var(--green)"/><rect x="210" width="30" height="3" fill="var(--yellow)"/></svg>
  <svg class="abs" style="left:10px;top:78px" width="364" height="90" viewBox="0 0 364 90" font-family="Poppins, sans-serif" text-anchor="middle">
    <line x1="37" y1="20" x2="346" y2="20" stroke="#ccc" stroke-width="1"/>
    <g font-size="5.5" font-weight="600" fill="var(--ink)">
      <text x="37" y="10">2015</text><text x="99" y="10">2016</text><text x="160" y="10">2017</text><text x="222" y="9">2018</text><text x="284" y="9">2019</text><text x="346" y="9">2020</text>
    </g>
    <circle cx="37" cy="20" r="4.5" fill="var(--yellow)"/><circle cx="99" cy="20" r="4.5" fill="var(--green)"/><circle cx="160" cy="20" r="4.5" fill="var(--teal)"/><circle cx="222" cy="20" r="4.5" fill="var(--yellow)"/><circle cx="284" cy="20" r="4.5" fill="var(--green)"/><circle cx="346" cy="20" r="4.5" fill="var(--teal)"/>
    <g font-size="4.4" font-weight="500" fill="var(--ink)">
      <text x="37" y="53">Project name</text><text x="99" y="53">Project name</text><text x="160" y="53">Project name</text><text x="222" y="53">Project name</text><text x="284" y="53">Project name</text><text x="346" y="53">Project name</text>
    </g>
    <g font-size="3.8" fill="#999">
      <text x="37" y="60">Lorem ipsum is simply</text><text x="37" y="65">dummy unknown printer</text><text x="37" y="70">took a galley of type</text>
      <text x="99" y="60">Lorem ipsum is simply</text><text x="99" y="65">dummy unknown printer</text><text x="99" y="70">took a galley of type</text>
      <text x="160" y="60">Lorem ipsum is simply</text><text x="160" y="65">dummy unknown printer</text><text x="160" y="70">took a galley of type</text>
      <text x="222" y="60">Lorem ipsum is simply</text><text x="222" y="65">dummy unknown printer</text><text x="222" y="70">took a galley of type</text>
      <text x="284" y="60">Lorem ipsum is simply</text><text x="284" y="65">dummy unknown printer</text><text x="284" y="70">took a galley of type</text>
      <text x="346" y="60">Lorem ipsum is simply</text><text x="346" y="65">dummy unknown printer</text><text x="346" y="70">took a galley of type</text>
    </g>
  </svg>
  <div class="pgnum">18</div><div class="ftr-copy">Copyright © | All Rights Reserved</div>
</section>
<section class="slide c3 r6">
  <div class="hdr"><div class="hdr-title">Price</div><div class="brand"><span class="brand-dot"></span><span class="brand-name">LUMORA</span></div></div>
  <svg class="stripe" viewBox="0 0 384 5" preserveAspectRatio="none"><rect width="150" height="5" fill="var(--ink)"/><rect x="150" width="30" height="3" fill="var(--teal)"/><rect x="180" width="30" height="3" fill="var(--green)"/><rect x="210" width="30" height="3" fill="var(--yellow)"/></svg>
  <div class="abs" style="left:40px;top:58px;width:86px;height:118px;box-shadow:0 1px 5px rgba(0,0,0,.15);text-align:center">
    <div style="background:var(--teal);color:#fff;font-size:5.5px;padding:6px 0">PLAN TITLE</div>
    <div style="font-size:14px;font-weight:600;margin-top:8px">$50.00</div>
    <div class="p p-grey" style="padding:6px 10px 0">Lorem ipsum dolor sit amet, nec an dictas equidem appellantur, ut has commune.</div>
    <div class="pill" style="position:absolute;left:15px;top:100px;width:56px;height:11px;background:var(--green);padding:0;justify-content:center;font-weight:500">More here</div>
  </div>
  <div class="abs" style="left:152px;top:58px;width:86px;height:118px;box-shadow:0 1px 5px rgba(0,0,0,.15);text-align:center">
    <div style="background:var(--teal);color:#fff;font-size:5.5px;padding:6px 0">PLAN TITLE</div>
    <div style="font-size:14px;font-weight:600;margin-top:8px">$150.00</div>
    <div class="p p-grey" style="padding:6px 10px 0">Lorem ipsum dolor sit amet, nec an dictas equidem appellantur, ut has commune.</div>
    <div class="pill" style="position:absolute;left:15px;top:100px;width:56px;height:11px;background:var(--green);padding:0;justify-content:center;font-weight:500">More here</div>
  </div>
  <div class="abs" style="left:266px;top:58px;width:86px;height:118px;box-shadow:0 1px 5px rgba(0,0,0,.15);text-align:center">
    <div style="background:var(--teal);color:#fff;font-size:5.5px;padding:6px 0">PLAN TITLE</div>
    <div style="font-size:14px;font-weight:600;margin-top:8px">$300.00</div>
    <div class="p p-grey" style="padding:6px 10px 0">Lorem ipsum dolor sit amet, nec an dictas equidem appellantur, ut has commune.</div>
    <div class="pill" style="position:absolute;left:15px;top:100px;width:56px;height:11px;background:var(--green);padding:0;justify-content:center;font-weight:500">More here</div>
  </div>
  <div class="pgnum">19</div><div class="ftr-copy">Copyright © | All Rights Reserved</div>
</section>

<!-- Row 7 -->
<section class="slide c1 r7">
  <div class="hdr"><div class="hdr-title">Table</div><div class="brand"><span class="brand-dot"></span><span class="brand-name">LUMORA</span></div></div>
  <svg class="stripe" viewBox="0 0 384 5" preserveAspectRatio="none"><rect width="150" height="5" fill="var(--ink)"/><rect x="150" width="30" height="3" fill="var(--teal)"/><rect x="180" width="30" height="3" fill="var(--green)"/><rect x="210" width="30" height="3" fill="var(--yellow)"/></svg>
  <svg class="abs" style="left:24px;top:66px" width="340" height="112" viewBox="0 0 340 112" font-family="Poppins, sans-serif" font-size="4.4" text-anchor="middle">
    <rect x="57" y="0" width="283" height="16" fill="var(--teal)"/>
    <rect x="0" y="16" width="57" height="96" fill="var(--green)"/>
    <g fill="#fff" font-weight="600"><text x="85" y="10">Title here</text><text x="142" y="10">Title here</text><text x="198" y="10">Title here</text><text x="255" y="10">Title here</text><text x="312" y="10">Title here</text></g>
    <g stroke="#e6e6e6" stroke-width=".6"><line x1="57" y1="32" x2="340" y2="32"/><line x1="57" y1="48" x2="340" y2="48"/><line x1="57" y1="64" x2="340" y2="64"/><line x1="57" y1="80" x2="340" y2="80"/><line x1="57" y1="96" x2="340" y2="96"/></g>
    <g fill="#fff" opacity=".8"><text x="28" y="26">Product</text><text x="28" y="42">Product</text><text x="28" y="58">Product</text><text x="28" y="74">Product</text><text x="28" y="90">Product</text><text x="28" y="106">Product</text></g>
    <g fill="#999">
      <text x="85" y="26">Title here</text><text x="142" y="26">Title here</text><text x="198" y="26">Title here</text><text x="312" y="26">$200</text>
      <text x="85" y="42">Title here</text><text x="142" y="42">Title here</text><text x="198" y="42">Title here</text><text x="312" y="42">$150</text>
      <text x="85" y="58">Title here</text><text x="142" y="58">Title here</text><text x="198" y="58">Title here</text><text x="312" y="58">$55</text>
      <text x="85" y="74">Title here</text><text x="142" y="74">Title here</text><text x="198" y="74">Title here</text><text x="312" y="74">$360</text>
      <text x="85" y="90">Title here</text><text x="142" y="90">Title here</text><text x="198" y="90">Title here</text><text x="312" y="90">$90</text>
      <text x="85" y="106">Title here</text><text x="142" y="106">Title here</text><text x="198" y="106">Title here</text><text x="312" y="106">$105</text>
    </g>
    <g fill="none" stroke-width=".9">
      <circle cx="255" cy="24.5" r="3.4" stroke="var(--yellow)"/><circle cx="255" cy="40.5" r="3.4" stroke="var(--yellow)"/>
      <circle cx="255" cy="56.5" r="3.4" stroke="var(--green)"/><circle cx="255" cy="72.5" r="3.4" stroke="var(--yellow)"/>
      <circle cx="255" cy="88.5" r="3.4" stroke="var(--green)"/><circle cx="255" cy="104.5" r="3.4" stroke="var(--green)"/>
      <path d="M253.3 56.7l1.3 1.3 2.2-2.4M253.3 88.7l1.3 1.3 2.2-2.4M253.3 104.7l1.3 1.3 2.2-2.4" stroke="var(--green)"/>
    </g>
  </svg>
  <div class="abs" style="left:16px;top:197px;width:352px;height:1px;background:#ddd"></div>
  <div class="pgnum">20</div><div class="ftr-copy">Copyright © | All Rights Reserved</div>
</section>
<section class="slide c2 r7">
  <div class="hdr"><div class="hdr-title">Our Team</div><div class="brand"><span class="brand-dot"></span><span class="brand-name">LUMORA</span></div></div>
  <svg class="stripe" viewBox="0 0 384 5" preserveAspectRatio="none"><rect width="150" height="5" fill="var(--ink)"/><rect x="150" width="30" height="3" fill="var(--teal)"/><rect x="180" width="30" height="3" fill="var(--green)"/><rect x="210" width="30" height="3" fill="var(--yellow)"/></svg>
  <div class="abs" style="left:31px;top:60px;width:94px;height:116px;box-shadow:0 1px 5px rgba(0,0,0,.15);text-align:center">
    <div style="background:var(--teal);color:#fff;font-size:5.5px;height:52px;padding-top:10px;line-height:1.5"><b>Add A Name</b><br>Founder</div>
    <div class="dot" style="left:27px;top:36px;width:40px;height:40px;background:var(--ink);border:2px solid #fff"></div>
    <div class="p p-grey" style="padding:30px 8px 0">Lorem ipsum dolor sit amet, consectetur adipiscing elit. Donec mauris lorem, vestibulum ac rutrum id, suscipit in dui.</div>
  </div>
  <div class="abs" style="left:147px;top:60px;width:94px;height:116px;box-shadow:0 1px 5px rgba(0,0,0,.15);text-align:center">
    <div style="background:var(--teal);color:#fff;font-size:5.5px;height:52px;padding-top:10px;line-height:1.5"><b>Add A Name</b><br>Founder</div>
    <div class="dot" style="left:27px;top:36px;width:40px;height:40px;background:var(--ink);border:2px solid #fff"></div>
    <div class="p p-grey" style="padding:30px 8px 0">Lorem ipsum dolor sit amet, consectetur adipiscing elit. Donec mauris lorem, vestibulum ac rutrum id, suscipit in dui.</div>
  </div>
  <div class="abs" style="left:262px;top:60px;width:94px;height:116px;box-shadow:0 1px 5px rgba(0,0,0,.15);text-align:center">
    <div style="background:var(--teal);color:#fff;font-size:5.5px;height:52px;padding-top:10px;line-height:1.5"><b>Add A Name</b><br>Founder</div>
    <div class="dot" style="left:27px;top:36px;width:40px;height:40px;background:var(--ink);border:2px solid #fff"></div>
    <div class="p p-grey" style="padding:30px 8px 0">Lorem ipsum dolor sit amet, consectetur adipiscing elit. Donec mauris lorem, vestibulum ac rutrum id, suscipit in dui.</div>
  </div>
  <div class="pgnum">21</div><div class="ftr-copy">Copyright © | All Rights Reserved</div>
</section>
<section class="slide c3 r7">
  <div class="hdr"><div class="hdr-title">Comparison Slide</div><div class="brand"><span class="brand-dot"></span><span class="brand-name">LUMORA</span></div></div>
  <svg class="stripe" viewBox="0 0 384 5" preserveAspectRatio="none"><rect width="180" height="5" fill="var(--ink)"/><rect x="180" width="30" height="3" fill="var(--teal)"/><rect x="210" width="30" height="3" fill="var(--green)"/><rect x="240" width="30" height="3" fill="var(--yellow)"/></svg>
  <div class="abs" style="left:24px;top:62px;font-size:5.5px">Lorem ipsum dolor</div>
  <div class="abs p p-grey" style="left:24px;top:71px;width:90px">Lorem ipsum dolor sit amet, consectetur adipiscing elit, sed do eiusmod tempor</div>
  <div class="abs p p-grey" style="left:24px;top:88px;width:90px">▸ Lorem ipsum dolor<br>▸ Sit amet consectetur adipiscing<br>▸ Do eiusmod tempor<br>▸ Et pero ipsum do<br>▸ Lorem ipsum dolor</div>
  <div class="abs" style="left:276px;top:62px;font-size:5.5px">Lorem ipsum dolor</div>
  <div class="abs p p-grey" style="left:276px;top:71px;width:90px">Lorem ipsum dolor sit amet, consectetur adipiscing elit, sed do eiusmod tempor</div>
  <div class="abs p p-grey" style="left:276px;top:88px;width:90px">▸ Lorem ipsum dolor<br>▸ Sit amet consectetur adipiscing<br>▸ Do eiusmod tempor<br>▸ Et pero ipsum do<br>▸ Lorem ipsum dolor</div>
  <svg class="abs" style="left:118px;top:68px" width="150" height="68" viewBox="0 0 150 68">
    <polygon points="0,20 28,0 28,12 70,12 70,28 28,28 28,40" fill="var(--teal)"/>
    <polygon points="8,48 36,28 36,40 70,40 70,56 36,56 36,68" fill="var(--teal)" opacity=".85"/>
    <polygon points="150,20 122,0 122,12 80,12 80,28 122,28 122,40" fill="var(--ink)"/>
    <polygon points="142,48 114,28 114,40 80,40 80,56 114,56 114,68" fill="var(--ink)"/>
    <circle cx="75" cy="34" r="20" fill="#fff"/>
  </svg>
  <div class="brand" style="left:178px;top:99px;color:var(--ink);gap:2px"><span class="brand-dot" style="width:4px;height:4px"></span><span class="brand-name" style="font-size:5.5px">LUMORA</span></div>
  <div class="abs" style="left:28px;top:158px;font-size:5.5px;display:flex;gap:24px;color:#555"><span>Lumora</span><span>Logo</span><span>Logo</span></div>
  <div class="abs" style="left:238px;top:158px;font-size:5.5px;display:flex;gap:28px;color:#555"><span>Logo</span><span>Logo</span><span>Logo</span></div>
  <div class="pgnum">22</div><div class="ftr-copy">Copyright © | All Rights Reserved</div>
</section>

<!-- Row 8 -->
<section class="slide c1 r8">
  <svg class="abs" style="left:22px;top:42px" width="180" height="130" viewBox="0 0 180 130" font-family="Poppins, sans-serif" font-size="4">
    <g stroke="#eee" stroke-width=".5"><line x1="5" y1="10" x2="175" y2="10"/><line x1="5" y1="40" x2="175" y2="40"/><line x1="5" y1="70" x2="175" y2="70"/><line x1="5" y1="100" x2="175" y2="100"/></g>
    <polyline fill="none" stroke="var(--green)" stroke-width="1.8" points="8,90 22,65 36,95 50,100 64,30 78,110 92,68 106,90 120,22 134,70 148,35 162,90"/>
    <polyline fill="none" stroke="var(--yellow)" stroke-width="1.8" points="8,85 22,100 36,80 50,70 64,108 78,48 92,100 106,55 120,85 134,105 148,40 162,88"/>
    <g fill="var(--ink)"><text x="18" y="60">4.4</text><text x="62" y="25">5.7</text><text x="116" y="17">6.7</text><text x="150" y="31">5.6</text><text x="86" y="64">3.2</text><text x="38" y="92">2.8</text><text x="52" y="110">1.6</text><text x="76" y="120">2</text><text x="104" y="100">2.9</text><text x="128" y="114">2.4</text><text x="4" y="96">2.4</text><text x="164" y="98">2.4</text></g>
    <g fill="#999" font-size="3.2"><text x="5" y="127">2009</text><text x="19" y="127">2010</text><text x="33" y="127">2011</text><text x="47" y="127">2012</text><text x="61" y="127">2013</text><text x="75" y="127">2014</text><text x="89" y="127">2015</text><text x="103" y="127">2016</text><text x="117" y="127">2017</text><text x="131" y="127">2018</text><text x="145" y="127">2019</text><text x="159" y="127">2020</text></g>
  </svg>
  <div class="abs" style="left:229px;top:48px;font-size:15px;font-weight:500">Chart</div>
  <div class="abs" style="left:229px;top:66px;font-size:7px;font-weight:300">Lorem ipsum dolor sit amet</div>
  <div class="abs" style="left:231px;top:86px;font-size:12px;font-weight:600;color:var(--yellow)">35 %</div>
  <div class="abs p" style="left:268px;top:89px;width:95px">Lorem ipsum dolor sit amet, consectetur adipiscing elit, sed do eiusmod tempor incididunt ut labore et dolore magna aliqua.</div>
  <div class="abs p" style="left:231px;top:112px;width:128px">▸ Lorem ipsum dolor sit amet, consectetur adipiscing elit, sed do eiusmod tempor incididunt ut labore et dolore magna aliqua.<br><br>▸ Lorem ipsum dolor sit amet, consectetur adipiscing elit. Lorem ipsum dolor sit amet, consectetur adipiscing elit.</div>
  <svg class="ftr" viewBox="0 0 384 14" preserveAspectRatio="none"><rect y="2" width="384" height="12" fill="var(--ink)"/><polygon points="150,0 210,0 214,3 154,3" fill="var(--yellow)"/><polygon points="210,0 270,0 274,3 214,3" fill="var(--green)"/><polygon points="270,0 384,0 384,3 274,3" fill="var(--teal)"/></svg>
  <div class="ftr-dark"><div class="ftr-copy">Copyright © | All Rights Reserved</div></div>
</section>
<section class="slide c2 r8" style="background:var(--teal)">
  <div class="abs" style="left:28px;top:92px;font-size:20px;font-weight:600;color:#fff">Page break</div>
  <div class="abs" style="left:28px;top:120px;width:20px;height:4px;border-radius:2px;background:var(--yellow)"></div>
  <div class="abs p" style="left:28px;top:130px;width:190px;color:#fff">Lorem ipsum dolor sit amet, consectetur adipiscing elit, sed do eiusmod tempor incididunt ut labore et dolore magna aliqua. Lorem ipsum dolor sit amet, consectetur adipiscing elit, sed do eiusmod tempor incididunt ut labore et dolore magna aliqua. Ut enim ad minim veniam, quis nostrud exercitation ullamco laboris nisi ut aliquip.</div>
</section>
<section class="slide c3 r8" style="background:#f7f7f7">
  <div class="abs" style="left:50px;top:42px;width:102px;height:22px;background:var(--green);color:#fff;font-size:4.2px;display:flex;align-items:center;padding-left:28px">www.lumora.example</div>
  <svg class="abs" style="left:60px;top:49px" width="9" height="9" viewBox="0 0 10 10"><circle cx="5" cy="5" r="4" fill="none" stroke="#fff" stroke-width="1"/><line x1="1" y1="5" x2="9" y2="5" stroke="#fff" stroke-width=".8"/><ellipse cx="5" cy="5" rx="1.8" ry="4" fill="none" stroke="#fff" stroke-width=".8"/></svg>
  <div class="abs" style="left:50px;top:66px;width:102px;height:24px;background:#fff;font-size:4px;display:flex;align-items:center;padding-left:28px;color:#555;line-height:1.4">Here to write your<br>Company adress</div>
  <svg class="abs" style="left:60px;top:73px" width="8" height="10" viewBox="0 0 8 10"><path d="M4 9.5C1.5 6 .5 4.5.5 3.5a3.5 3.5 0 0 1 7 0c0 1-1 2.5-3.5 6z" fill="none" stroke="var(--green)" stroke-width=".9"/><circle cx="4" cy="3.5" r="1.1" fill="var(--green)"/></svg>
  <div class="abs" style="left:50px;top:92px;width:102px;height:24px;background:#fff;font-size:4.2px;display:flex;align-items:center;padding-left:28px;color:#555">(371) 555-0142</div>
  <svg class="abs" style="left:60px;top:99px" width="9" height="9" viewBox="0 0 10 10"><path d="M2.2 1l1.8 2-1 1.2c.7 1.4 1.5 2.2 2.9 2.9L7 6l2 1.8-1.2 1.5C4.5 9 1 5.5.8 2.2z" fill="var(--green)"/></svg>
  <div class="abs" style="left:50px;top:118px;width:102px;height:24px;background:#fff;font-size:4.2px;display:flex;align-items:center;padding-left:28px;color:#555">hello@lumora.example</div>
  <svg class="abs" style="left:60px;top:126px" width="10" height="8" viewBox="0 0 10 8"><rect x=".5" y=".5" width="9" height="7" fill="none" stroke="var(--green)" stroke-width=".9"/><path d="M.5.5L5 4.5 9.5.5" fill="none" stroke="var(--green)" stroke-width=".9"/></svg>
  <div class="brand" style="left:196px;top:102px;color:var(--ink);gap:6px"><span class="brand-dot" style="width:10px;height:10px"></span><span class="brand-name" style="font-size:15px">LUMORA</span></div>
</section>

</body>
</html>
```